body balm label design

body balm tube design, current label design for other similar products
Need to have a design which can interchange between 3 different solutions
Amber Tide (Lavender + Vanilla)
Copper Harbor (Eucalyptus + Mint)
Velvet Arc (Bergamot + Cedarwood)
Tube size:
2.5h x 3.25 w
Target Market(s)
natural, solution focused
Requirements
Must have
- relatable to existing brand designs, focus on features and benefits

```html
<!DOCTYPE html>
<html lang="en">
<head>
<meta charset="utf-8">
<title>Willow Bloom Natural Body Spray Labels</title>
<link href="https://fonts.googleapis.com/css2?family=Playfair+Display&family=Roboto+Condensed:wght@300&family=Sacramento&family=Tinos&display=swap" rel="stylesheet">
<style>
  :root {
    --backdrop: #c8cac8;
    --label: #ffffff;
    --tab: #4b4b4b;
    --title: #8c8c8c;
    --rule: #8c8c8c;
    --ink: #777777;
    --soft: #9a9a9a;
  }
  * { margin: 0; padding: 0; box-sizing: border-box; }
  html, body { width: 1200px; height: 499px; overflow: hidden; background: var(--backdrop); }
  .sheet { position: relative; width: 1200px; height: 499px; }

  .label {
    position: absolute; top: 124px; width: 273px; height: 251px;
    background: var(--label); overflow: hidden;
  }
  .label--amber { left: 146px; --accent-top: #a56c9f; --accent-script: #e2cf3f; --art-a: #d9c34a; --art-b: #4b4b4b; }
  .label--copper { left: 472px; --accent-top: #2f7a55; --accent-script: #66b64c; --art-a: #3f7a55; --art-b: #4b4b4b; }
  .label--velvet { left: 778px; --accent-top: #5e9a63; --accent-script: #9a6b34; --art-a: #c68a3c; --art-b: #4b4b4b; }

  .rule-top, .rule-bottom { position: absolute; left: 40px; width: 1.3px; background: var(--rule); }
  .rule-top { top: 0; height: 20px; }
  .rule-bottom { top: 231px; height: 20px; }

  .rot {
    position: absolute; white-space: nowrap;
    transform: translate(-50%, -50%) rotate(-90deg);
  }
  .product-name {
    position: absolute; left: 41px; top: 126px; white-space: nowrap;
    transform: translate(-50%, -50%) rotate(-90deg) scaleX(0.68);
    font-family: "Playfair Display", serif; font-weight: 400; font-size: 29px; line-height: 1;
    color: var(--title); letter-spacing: 0.5px; text-transform: uppercase;
  }

  .tab { position: absolute; left: 82px; top: -1px; width: 59px; height: 132px; }
  .tab svg { display: block; }
  .brand {
    position: absolute; left: 82px; top: 11px; width: 59px; text-align: center;
    font-family: "Tinos", serif; font-size: 4.3px; letter-spacing: 0.6px; color: #e8e8e8;
  }
  .tab-title {
    position: absolute; left: 82px; top: 33px; width: 59px; text-align: center;
    font-family: "Roboto Condensed", sans-serif; font-weight: 300; color: #ffffff;
    font-size: 7.2px; line-height: 8.4px;
  }
  .tab-title .spaced { letter-spacing: 1.6px; }
  .scent-art {
    position: absolute; left: 96px; top: 58px; width: 32px; height: 32px; border-radius: 50%;
    background: radial-gradient(circle, var(--art-a) 0%, var(--art-b) 72%);
    opacity: 0.75;
  }

  .scent {
    position: absolute; left: 112px; transform: translateX(-50%); white-space: nowrap; text-align: center;
  }
  .scent-top {
    top: 164px; font-family: "Tinos", serif; font-size: 9.2px; letter-spacing: 0.8px;
    color: var(--accent-top);
  }
  .scent-script {
    top: 174px; font-family: "Sacramento", cursive; font-size: 27px; line-height: 1;
    color: var(--accent-script);
  }

  .origin-seal {
    position: absolute; left: 142px; top: 215px; width: 16px; height: 16px;
    border: 0.6px solid #b5b5b5; border-radius: 50%;
  }
  .net-weight {
    position: absolute; left: 112px; top: 238px; transform: translateX(-50%);
    font-family: "Tinos", serif; font-size: 4.3px; color: var(--ink); white-space: nowrap;
  }

  .claims-rule { position: absolute; left: 206px; top: 14px; width: 0.8px; height: 224px; background: var(--soft); }
  .claims {
    left: 196px; top: 125px; width: 226px;
    display: flex; justify-content: space-between; align-items: center;
    font-family: "Sacramento", cursive; font-size: 13px; line-height: 1; color: var(--soft);
  }
  .claims .dot { font-family: "Tinos", serif; font-size: 5px; }

  .ingredients-head {
    left: 212px; top: 124px;
    font-family: "Tinos", serif; font-size: 5.6px; color: var(--ink);
  }
  .ingredients {
    left: 237px; top: 126px; width: 222px; white-space: normal;
    font-family: "Tinos", serif; font-size: 4.6px; line-height: 5.2px; color: var(--ink);
    text-align: right;
  }

  .social { position: absolute; left: 263px; top: 37px; width: 4px; }
  .social span { display: block; width: 3.4px; height: 3.4px; border-radius: 50%; background: #9c9c9c; margin-bottom: 1.4px; }
  .maker {
    left: 265px; top: 122px;
    font-family: "Tinos", serif; font-size: 3.6px; color: var(--ink);
  }
  .site {
    left: 265px; top: 198px;
    font-family: "Tinos", serif; font-size: 3.6px; color: var(--ink);
  }
</style>
</head>
<body>
<main class="sheet">

  <section class="label label--amber">
    <div class="rule-top"></div><div class="rule-bottom"></div>
    <h1 class="product-name">Amber Tide</h1>
    <div class="tab">
      <svg width="59" height="132" viewBox="0 0 59 132">
        <path d="M0 0 H59 V102.5 A29.5 29.5 0 0 1 0 102.5 Z" fill="var(--tab)"/>
        <path id="arc-amber" d="M3 102 A26.5 26.5 0 0 0 56 102" fill="none"/>
        <text font-family="Tinos, serif" font-size="3.6" fill="#eeeeee" letter-spacing="0.3"><textPath href="#arc-amber" startOffset="50%" text-anchor="middle">PLANT · BASED · AROMATHERAPY</textPath></text>
      </svg>
    </div>
    <div class="brand">WILLOW BLOOM</div>
    <div class="tab-title"><span class="spaced">NATURAL</span><br>BODY SPRAY</div>
    <div class="scent-art" role="img" aria-label="Line drawing of vanilla pods and flower"></div>
    <p class="scent scent-top">LAVENDER +</p>
    <p class="scent scent-script">Vanilla</p>
    <div class="origin-seal"></div>
    <p class="net-weight">Net WT. 3oz</p>
    <div class="claims-rule"></div>
    <div class="rot claims"><span>Plant Based</span><span class="dot">·</span><span>Vegan</span><span class="dot">·</span><span>Cruelty Free</span></div>
    <p class="rot ingredients-head">Ingredients</p>
    <p class="rot ingredients">Lorem Ipsum is simply dummy text of the printing and typesetting industry. Lorem Ipsum has been the industry's standard dummy text ever since the 1500s, when an unknown printer took a galley of type and scrambled it to make a type specimen book. It has survived not only five centuries, but also the leap into electronic typesetting, remaining essentially unchanged.</p>
    <div class="social"><span></span><span></span><span></span><span></span></div>
    <p class="rot maker">Made by Willow Bloom, Fernvale, AB T0A 0A0</p>
    <p class="rot site">www.willowbloom.ca</p>
  </section>

  <section class="label label--copper">
    <div class="rule-top"></div><div class="rule-bottom"></div>
    <h1 class="product-name">Copper Harbor</h1>
    <div class="tab">
      <svg width="59" height="132" viewBox="0 0 59 132">
        <path d="M0 0 H59 V102.5 A29.5 29.5 0 0 1 0 102.5 Z" fill="var(--tab)"/>
        <path id="arc-copper" d="M3 102 A26.5 26.5 0 0 0 56 102" fill="none"/>
        <text font-family="Tinos, serif" font-size="3.6" fill="#eeeeee" letter-spacing="0.3"><textPath href="#arc-copper" startOffset="50%" text-anchor="middle">PLANT · BASED · AROMATHERAPY</textPath></text>
      </svg>
    </div>
    <div class="brand">WILLOW BLOOM</div>
    <div class="tab-title"><span class="spaced">NATURAL</span><br>BODY SPRAY</div>
    <div class="scent-art" role="img" aria-label="Line drawing of mint leaves"></div>
    <p class="scent scent-top">EUCALYPTUS +</p>
    <p class="scent scent-script">Mint</p>
    <div class="origin-seal"></div>
    <p class="net-weight">Net WT. 3oz</p>
    <div class="claims-rule"></div>
    <div class="rot claims"><span>Plant Based</span><span class="dot">·</span><span>Vegan</span><span class="dot">·</span><span>Cruelty Free</span></div>
    <p class="rot ingredients-head">Ingredients</p>
    <p class="rot ingredients">Lorem Ipsum is simply dummy text of the printing and typesetting industry. Lorem Ipsum has been the industry's standard dummy text ever since the 1500s, when an unknown printer took a galley of type and scrambled it to make a type specimen book. It has survived not only five centuries, but also the leap into electronic typesetting, remaining essentially unchanged.</p>
    <div class="social"><span></span><span></span><span></span><span></span></div>
    <p class="rot maker">Made by Willow Bloom, Fernvale, AB T0A 0A0</p>
    <p class="rot site">www.willowbloom.ca</p>
  </section>

  <section class="label label--velvet">
    <div class="rule-top"></div><div class="rule-bottom"></div>
    <h1 class="product-name">Velvet Arc</h1>
    <div class="tab">
      <svg width="59" height="132" viewBox="0 0 59 132">
        <path d="M0 0 H59 V102.5 A29.5 29.5 0 0 1 0 102.5 Z" fill="var(--tab)"/>
        <path id="arc-velvet" d="M3 102 A26.5 26.5 0 0 0 56 102" fill="none"/>
        <text font-family="Tinos, serif" font-size="3.6" fill="#eeeeee" letter-spacing="0.3"><textPath href="#arc-velvet" startOffset="50%" text-anchor="middle">PLANT · BASED · AROMATHERAPY</textPath></text>
      </svg>
    </div>
    <div class="brand">WILLOW BLOOM</div>
    <div class="tab-title"><span class="spaced">NATURAL</span><br>BODY SPRAY</div>
    <div class="scent-art" role="img" aria-label="Line drawing of a cedar cone"></div>
    <p class="scent scent-top">BERGAMOT +</p>
    <p class="scent scent-script">Cedarwood</p>
    <div class="origin-seal"></div>
    <p class="net-weight">Net WT. 3oz</p>
    <div class="claims-rule"></div>
    <div class="rot claims"><span>Plant Based</span><span class="dot">·</span><span>Vegan</span><span class="dot">·</span><span>Cruelty Free</span></div>
    <p class="rot ingredients-head">Ingredients</p>
    <p class="rot ingredients">Lorem Ipsum is simply dummy text of the printing and typesetting industry. Lorem Ipsum has been the industry's standard dummy text ever since the 1500s, when an unknown printer took a galley of type and scrambled it to make a type specimen book. It has survived not only five centuries, but also the leap into electronic typesetting, remaining essentially unchanged.</p>
    <div class="social"><span></span><span></span><span></span><span></span></div>
    <p class="rot maker">Made by Willow Bloom, Fernvale, AB T0A 0A0</p>
    <p class="rot site">www.willowbloom.ca</p>
  </section>

</main>
</body>
</html>
```